Children's Party Business needs a Business Card design!

We need a double sided, colour business card design.
The company name is "Maplewood Kids' Celebrations". We want one side to feature this logo.
We want the second side to feature the two branches "The Caped Crusade Adventure" and "The Fairytale Gala Adventure". I have attached logos for each of these below. When using these, I suggest removing the tagline & image from the logos, as those elements are already featured in the "Maplewood Kids' Celebration" logo.
To be included:
www.maplewoodkidscelebrations.com.au
1300 471 608
Optional text- "Making Dreams a Reality"
Optional photos- I've attached a bunch of our Character photos, which can be used if you please!
To give you an idea of the business, see The Caped Crusade Adventure website (under development):
http://qorvint.com/demo/capedcrusadeadventure/
Target Market(s)
Parents
Industry/Entity Type
Business
Contact Information for Business Card
To be included:
1300 471 608
Colors
Designer to choose colors to be used in the design.
Look and feel

```html
<!DOCTYPE html>
<html lang="en">
<head>
<meta charset="utf-8">
<title>Maplewood Kids' Celebrations – Business Card</title>
<link rel="stylesheet" href="https://fonts.googleapis.com/css2?family=Arimo:wght@400;700&family=Fredoka:wght@600&display=swap">
<style>
  :root {
    --page-bg: #2b2b2d;
    --card-white: #ffffff;
    --card-shade: #eef0f3;
    --navy: #123f7a;
    --navy-deep: #0c2d5c;
    --sky: #6fa9dc;
    --sky-light: #9cc6ea;
    --brand-ink: #1d4a86;
    --photo-a: #8d7f7a;
    --photo-b: #5d6f88;
    --white-text: #ffffff;
  }
  * { box-sizing: border-box; margin: 0; padding: 0; }
  html, body { width: 1200px; height: 997px; overflow: hidden; }
  body {
    background: var(--page-bg);
    font-family: "Arimo", Arial, sans-serif;
    position: relative;
  }
  .card {
    position: absolute;
    width: 700px;
    height: 400px;
    left: 250px;
    border-radius: 22px;
    overflow: hidden;
    background: linear-gradient(180deg, var(--card-white) 0%, var(--card-shade) 100%);
    box-shadow: 0 14px 30px rgba(0,0,0,0.45);
  }
  .card--back { top: 62px; }
  .card--front { top: 535px; }
  .card svg.card-art { position: absolute; inset: 0; width: 100%; height: 100%; }

  /* Back side */
  .branch {
    position: absolute;
    display: flex;
    align-items: center;
    gap: 10px;
    font-family: "Fredoka", "Arimo", sans-serif;
    font-weight: 600;
    font-size: 24px;
    color: var(--brand-ink);
    line-height: 1.1;
  }
  .branch__dot {
    width: 16px; height: 16px; border-radius: 50%;
    background: var(--sky); flex: none;
  }
  .branch--caped { top: 30px; right: 40px; text-align: right; }
  .branch--fairytale { top: 112px; left: 34px; }

  /* Front side */
  .brand {
    position: absolute;
    top: 70px; left: 0; right: 0;
    display: flex; justify-content: center; align-items: center; gap: 16px;
  }
  .brand__mark {
    width: 54px; height: 54px; border-radius: 50%;
    background: var(--navy); flex: none;
  }
  .brand__name {
    font-family: "Fredoka", "Arimo", sans-serif;
    font-weight: 600;
    font-size: 44px;
    color: var(--brand-ink);
    line-height: 1;
    max-width: 470px;
  }
  .tagline {
    position: absolute;
    top: 276px; left: 190px; width: 290px;
    text-align: center;
    font-weight: 700; font-size: 17px; letter-spacing: 1px;
    color: var(--navy-deep);
  }
  .contact {
    position: absolute;
    display: flex; align-items: center; gap: 10px;
    color: var(--white-text);
    font-size: 17px; font-weight: 700;
  }
  .contact svg { width: 26px; height: 26px; flex: none; }
  .contact--web { left: 34px; bottom: 34px; }
  .contact--phone { right: 34px; top: 262px; }
</style>
</head>
<body>

<section class="card card--back" aria-label="Card back">
  <svg class="card-art" viewBox="0 0 700 400">
    <defs>
      <linearGradient id="photoTones" x1="0" x2="1" y1="0" y2="0">
        <stop offset="0" stop-color="var(--photo-b)"/>
        <stop offset="0.5" stop-color="var(--photo-a)"/>
        <stop offset="1" stop-color="var(--photo-b)"/>
      </linearGradient>
    </defs>
    <g transform="rotate(-18 350 230)">
      <rect x="-120" y="250" width="940" height="150" fill="var(--navy)"/>
      <rect x="-120" y="250" width="940" height="32" fill="var(--navy-deep)"/>
      <text x="330" y="272" fill="#ffffff" font-family="Arimo, sans-serif" font-weight="700" font-size="15" letter-spacing="2">Wide range of characters to choose from</text>
      <rect x="-100" y="288" width="900" height="104" fill="url(#photoTones)" role="img" aria-label="Strip of photographs of costumed party characters"/>
    </g>
  </svg>
  <div class="branch branch--caped"><span class="branch__dot"></span><span>The Caped Crusade<br>Adventure</span></div>
  <div class="branch branch--fairytale"><span class="branch__dot"></span><span>The Fairytale Gala<br>Adventure</span></div>
</section>

<section class="card card--front" aria-label="Card front">
  <svg class="card-art" viewBox="0 0 700 400">
    <polygon points="0,310 470,310 530,225 700,225 700,400 0,400" fill="var(--navy)"/>
    <polygon points="140,310 182,258 500,258 464,310" fill="var(--sky-light)"/>
    <polygon points="160,304 192,266 488,266 460,304" fill="var(--sky)"/>
  </svg>
  <div class="brand">
    <span class="brand__mark"></span>
    <span class="brand__name">Maplewood Kids' Celebrations</span>
  </div>
  <p class="tagline">MAKING DREAMS A REALITY</p>
  <p class="contact contact--phone">
    <svg viewBox="0 0 26 26"><circle cx="13" cy="13" r="12" fill="var(--sky-light)"/><path d="M8 9c0 5 4 9 9 9l1.5-2-2.5-1.5-1.2 1c-1.8-.8-3.3-2.3-4.1-4.1l1-1.2L10.2 7.5z" fill="var(--navy)"/></svg>
    1300 471 608
  </p>
  <p class="contact contact--web">
    <svg viewBox="0 0 26 26"><circle cx="13" cy="13" r="12" fill="var(--sky-light)"/><path d="M7 13l6-5 6 5h-2v5h-8v-5z" fill="var(--navy)"/></svg>
    www.maplewoodkidscelebrations.com.au
  </p>
</section>

</body>
</html>
```